Customer Hotel Entertainment Rack Card 4 X 9

Design a rack card for hotel display cases. Need the top of card on both sides to draw attention. The top inch and a half to two inches is what customers see when deciding on what brochure to select. We want it to draw attention and look as fun as it really is. <br/><br/>We are a boat rental company that does guided boat tours for 3 to 3 and half hours to a beautiful uninhabited island that is surrounded by mangroves and palm trees. Dolphin and manatee can be seen swimming in the water. The wildlife is active and amazing. The boats are two seater power boats allowing the customer to drive their own boat while following a guide. <br/><br/>We offer pontoon boats for rent and the two seater power boats. We rent for half day or full day. <br/><br/>I have uploaded lots of photos to help. We want it to look super fun and attractive .

Target Market(s)

Tourists, Vaction Entertainment, Water Fun, Beach goers

Colors

Designer to choose colors to be used in the design.

Requirements
Must have
• Business Info
• Coral Drifter Boat Rental and Tours
• 418 Wrenfield Drive
• Naples, FL 34114
• Phone Number: 239.555.0186
• www.coraldrifterboatrentalandtours.example

```html
<!DOCTYPE html>
<html lang="en">
<head>
<meta charset="utf-8">
<title>Coral Drifter Boat Rental and Tours – Rack Card</title>
<link rel="stylesheet" href="https://fonts.googleapis.com/css2?family=Montserrat:wght@500;600;700&family=Titan+One&display=swap">
<style>
  :root{
    --page:#e4e4e4;
    --paper:#ffffff;
    --paper-back:#efeeeb;
    --orange:#c9623a;
    --orange-deep:#b8532d;
    --gold:#f6a623;
    --yellow:#ffd23a;
    --ink:#1e1e1e;
    --white:#ffffff;
  }
  *{box-sizing:border-box;margin:0;padding:0}
  html,body{width:1200px;height:1200px;overflow:hidden;background:var(--page)}
  body{position:relative;font-family:"Montserrat",sans-serif;color:var(--ink)}
  .card{position:absolute;top:100px;width:444px;height:1000px;overflow:hidden;box-shadow:0 10px 28px rgba(0,0,0,.25)}
  .card--front{left:120px;background:var(--paper)}
  .card--back{left:636px;background:var(--paper-back)}
  .photo{position:absolute}
  .shapes{position:absolute;left:0;top:0}

  /* front */
  .front-hero{left:0;top:0;width:444px;height:290px;background:linear-gradient(180deg,#6b5a7c 0%,#d96a4a 38%,#f08a4e 52%,#3a2a30 62%,#2b3440 100%)}
  .front-badge{position:absolute;left:90px;top:238px;width:220px;height:108px;border-radius:50%;background:var(--white);border:2px solid var(--orange);display:flex;align-items:center;justify-content:center;gap:8px}
  .front-badge .dot{width:16px;height:16px;border-radius:50%;background:var(--gold)}
  .front-badge .name{font-weight:700;font-size:20px;color:var(--orange)}
  .front-title{position:absolute;left:0;top:368px;width:444px;text-align:center;color:var(--white);font-weight:600;font-size:36px;line-height:1.08;letter-spacing:.5px}
  .front-marina{left:0;top:520px;width:444px;height:300px;background:linear-gradient(180deg,#5f8a48 0%,#3c4c55 22%,#27323b 55%,#8a9198 80%,#ffffff 100%)}
  .front-copy{position:absolute;left:30px;top:780px;width:384px;text-align:center;font-size:13.5px;font-weight:500;line-height:1.3}
  .front-url{position:absolute;left:0;top:884px;width:444px;height:40px;background:var(--orange);color:var(--white);font-weight:700;font-size:16px;display:flex;align-items:center;justify-content:center}
  .front-url span{color:var(--gold)}
  .front-map{left:0;top:924px;width:444px;height:76px;background:linear-gradient(135deg,#3e4a34,#1f2a26 60%,#4f5b45)}

  /* back */
  .back-hero{left:0;top:0;width:444px;height:200px;background:linear-gradient(180deg,#f3b07a 0%,#f7c467 40%,#2c2418 62%,#6a5a3a 100%)}
  .back-map{left:0;top:196px;width:236px;height:200px;background:linear-gradient(90deg,#3f7a5c 0%,#5a8f6e 55%,rgba(239,238,235,0) 100%)}
  .tag{display:inline-block;background:var(--orange);color:var(--white);font-family:"Titan One",sans-serif;font-size:14px;line-height:1;padding:4px 10px;margin-bottom:3px}
  .tags{position:absolute;text-align:center}
  .blurb{position:absolute;font-size:10.5px;line-height:1.25;text-align:center}
  .eco-tags{left:236px;top:212px;width:200px}
  .eco-copy{left:240px;top:290px;width:192px}
  .pontoon-photo{left:220px;top:404px;width:224px;height:210px;background:linear-gradient(180deg,#6a7f8f 0%,#9aa6ae 40%,#c9cbcc 70%,rgba(239,238,235,0) 100%)}
  .pontoon-tags{left:30px;top:450px;width:180px}
  .pontoon-copy{left:26px;top:506px;width:188px}
  .skim-photo{left:0;top:620px;width:250px;height:220px;background:linear-gradient(135deg,#e8ddc8 0%,#cfcbc0 45%,#a9b4bd 75%,rgba(239,238,235,0) 100%)}
  .skim-tags{left:256px;top:630px;width:180px}
  .skim-copy{left:254px;top:688px;width:184px}
  .strip{top:842px;height:86px;width:144px}
  .strip-1{left:4px;background:linear-gradient(180deg,#7d8a90,#5b6a72)}
  .strip-2{left:150px;background:linear-gradient(180deg,#8fb8d8 0%,#cfe0ea 45%,#e8dcc2 100%)}
  .strip-3{left:296px;background:linear-gradient(180deg,#d8cfbf,#b9b0a2)}
  .back-brand{position:absolute;left:14px;top:946px;display:flex;align-items:center;gap:7px}
  .back-brand .dot{width:14px;height:14px;border-radius:50%;background:var(--gold)}
  .back-brand .name{font-weight:700;font-size:15px;color:var(--orange)}
  .contact{position:absolute;left:176px;top:932px;width:260px;height:62px;background:var(--orange);color:var(--white);font-size:9.2px;font-weight:500;padding:6px 8px;list-style:none}
  .contact li{display:flex;align-items:center;gap:5px;line-height:12.5px}
  .contact svg{flex:none}
</style>
</head>
<body>

<article class="card card--front">
  <div class="photo front-hero" role="img" aria-label="Photo of a two-seater power boat speeding across the water at sunset"></div>
  <div class="photo front-marina" role="img" aria-label="Aerial photo of the marina with docked boats and mangroves"></div>
  <svg class="shapes" width="444" height="560" viewBox="0 0 444 560" aria-hidden="true">
    <path d="M0 262 Q222 188 444 222 L444 244 Q222 212 0 284 Z" fill="var(--gold)"/>
    <path d="M0 282 Q222 210 444 242 L444 504 Q222 470 0 548 Z" fill="var(--orange)"/>
    <path d="M0 548 Q222 470 444 504 L444 518 Q222 486 0 560 Z" fill="var(--white)"/>
    <path d="M0 542 Q222 466 444 498 L444 508 Q222 476 0 552 Z" fill="var(--gold)"/>
  </svg>
  <div class="front-badge"><span class="dot"></span><span class="name">Coral Drifter</span></div>
  <h1 class="front-title">coral drifter boat<br>rental and tours</h1>
  <p class="front-copy">Guided boat tours leaving Harbor Palms Marina, Naples, Florida touring the Everglades and the Ten Thousand Islands area. See Manatee, Dolphin and enjoy lots of shelling on uninhabited islands. Rent a pontoon boat and explore on your own at your own pace.</p>
  <div class="front-url">www.<span>coraldrifterboatrentalandtours</span>.example</div>
  <div class="photo front-map" role="img" aria-label="Satellite map of the marina canals"></div>
</article>

<article class="card card--back">
  <div class="photo back-hero" role="img" aria-label="Photo of palm trees and docked boats reflected at sunset"></div>
  <svg class="shapes" width="444" height="220" viewBox="0 0 444 220" aria-hidden="true">
    <path d="M0 190 Q260 200 444 110 L444 220 L0 220 Z" fill="var(--paper-back)"/>
    <path d="M0 180 Q260 192 444 100 L444 112 Q260 204 0 194 Z" fill="var(--orange)"/>
    <path d="M0 194 Q260 204 444 112 L444 118 Q260 210 0 200 Z" fill="var(--yellow)"/>
  </svg>
  <div class="photo back-map" role="img" aria-label="Aerial map of the island cluster around Whitehorse Key"></div>
  <div class="tags eco-tags"><span class="tag">Lets Go On</span><br><span class="tag">An Eco Adventure</span><br><span class="tag">to Whitehorse Key</span></div>
  <p class="blurb eco-copy">Whitehorse Key is a great place to beach the boats and find amazing shells. Walk the island and explore or you can just sit and relax. The beach has a great view of the Gulf of Mexico and dolphins are often seen swimming in the water next to shore.</p>

  <div class="photo pontoon-photo" role="img" aria-label="Photo of a pontoon boat docked at the marina"></div>
  <div class="tags pontoon-tags"><span class="tag">Pontoon Boat</span><br><span class="tag">Rental</span></div>
  <p class="blurb pontoon-copy">Rent a pontoon for a full day of fun. Explore on your own and head to an uninhabited island collecting shells or fish. Rent from 8-4pm</p>

  <div class="photo skim-photo" role="img" aria-label="Photo of a two-seater catamaran power boat beached on the sand"></div>
  <div class="tags skim-tags"><span class="tag">SkimCat</span><br><span class="tag">Rental</span></div>
  <p class="blurb skim-copy">Rent your very own SkimCat powerboat for 3 or 4 hours. Do some Eco touring on your own looking for manatee, dolphin, alligators and everything the Everglades has to offer. See the 10,000 islands up close.</p>

  <div class="photo strip strip-1" role="img" aria-label="Photo of an alligator swimming in the water"></div>
  <div class="photo strip strip-2" role="img" aria-label="Photo of small power boats beached on an island"></div>
  <div class="photo strip strip-3" role="img" aria-label="Photo of a beach find held up on the sand"></div>

  <div class="back-brand"><span class="dot"></span><span class="name">Coral Drifter</span></div>
  <ul class="contact">
    <li><svg width="9" height="10" viewBox="0 0 10 12"><path d="M5 0a4 4 0 0 0-4 4c0 3 4 8 4 8s4-5 4-8a4 4 0 0 0-4-4zm0 5.5A1.5 1.5 0 1 1 5 2.5a1.5 1.5 0 0 1 0 3z" fill="#fff"/></svg>418 Wrenfield Drive, Naples, FL 34114</li>
    <li><svg width="9" height="10" viewBox="0 0 12 10"><rect x="0.5" y="0.5" width="11" height="9" fill="none" stroke="#fff"/><path d="M0.5 0.5 6 5.5 11.5 0.5" fill="none" stroke="#fff"/></svg>coraldrifterinfo@example.com</li>
    <li><svg width="9" height="10" viewBox="0 0 12 12"><path d="M2.5 0.5 5 3 3.6 4.6a7 7 0 0 0 3.8 3.8L9 7l2.5 2.5-1.7 2C5 11 1 7 0.5 2.2z" fill="#fff"/></svg>239.555.0186</li>
    <li><svg width="9" height="10" viewBox="0 0 12 12"><circle cx="6" cy="6" r="5.4" fill="none" stroke="#fff"/><path d="M0.6 6h10.8M6 0.6c-3 3-3 7.8 0 10.8M6 0.6c3 3 3 7.8 0 10.8" fill="none" stroke="#fff" stroke-width=".8"/></svg>www.coraldrifterboatrentalandtours.example</li>
  </ul>
</article>

</body>
</html>
```